New Business Card Design Project

Updated business card design. I am moving towards more coaching of, for the most part women, who are searching for more in their lives. I am an intuitive healer, homeopath and nutritionist but also an author and motivational speaker. Int the past I have included my photo on the card but that is not essential. My book is called the Brilliance of Saffron - Reclaiming the Shade of Your Spirit so my colours are typically magenta.
Target Market(s)
Women - 35 - 60 considering improving their health. However, I am also a professional speaker with a target audience including corporate and conferences.
Industry/Entity Type
Health And Wellness
Contact Information for Business Card
Lucinda Parvell, CCH, CNP, MA
www.lucindaparvell.com
lucinda@lucindaparvell.com
519-362-7015
Facebook, instagram and twitter logos
Look and feel
Each slider illustrates characteristics of the customer's brand and the style your logo design should communicate.

```html
<!DOCTYPE html>
<html lang="en">
<head>
<meta charset="utf-8">
<title>Lucinda Parvell – Business Card</title>
<link rel="stylesheet" href="https://fonts.googleapis.com/css2?family=Lato:wght@400;700;900&display=swap">
<style>
  :root {
    --backdrop: #ececec;
    --card-white: #ffffff;
    --stripe: #f3f3f3;
    --magenta: #e5226f;
    --blush: #f7dbe6;
    --ink: #1a1a1a;
    --band-black: #111111;
    --photo-green: #4f6b3a;
    --photo-brick: #b89a78;
    --photo-light: #e9e4dc;
  }
  html, body {
    margin: 0;
    padding: 0;
    width: 1200px;
    height: 961px;
    overflow: hidden;
    background: var(--backdrop);
    font-family: "Lato", sans-serif;
  }
  .card {
    position: absolute;
    left: 50px;
    top: 150px;
    width: 1100px;
    height: 661px;
    display: block;
  }
  .name { font-family: "Lato", sans-serif; font-weight: 400; fill: var(--ink); }
  .tagline { font-family: "Lato", sans-serif; font-weight: 400; fill: var(--ink); }
  .credentials { font-family: "Lato", sans-serif; font-weight: 400; fill: var(--magenta); }
  .contact { font-family: "Lato", sans-serif; font-weight: 400; fill: var(--ink); }
  .website { font-family: "Lato", sans-serif; font-weight: 900; fill: var(--ink); letter-spacing: 1.2px; }
  .accent { fill: var(--magenta); }
</style>
</head>
<body>
<svg class="card" viewBox="0 0 626 376" xmlns="http://www.w3.org/2000/svg" aria-label="Business card for Lucinda Parvell">
  <defs>
    <linearGradient id="portrait-tones" x1="0" y1="0" x2="1" y2="0">
      <stop offset="0" stop-color="var(--photo-green)"/>
      <stop offset="0.45" stop-color="var(--photo-light)"/>
      <stop offset="1" stop-color="var(--photo-brick)"/>
    </linearGradient>
    <pattern id="fine-stripes" width="6" height="6" patternUnits="userSpaceOnUse" patternTransform="rotate(45)">
      <rect width="6" height="6" fill="var(--card-white)"/>
      <rect width="1" height="6" fill="var(--stripe)"/>
    </pattern>
  </defs>

  <rect class="portrait" x="330" y="0" width="296" height="376" fill="url(#portrait-tones)" role="img" aria-label="Portrait photo of Lucinda Parvell standing by a brick wall and greenery"/>

  <path class="band-magenta" d="M0 0 H383 C405 60 405 150 392 220 C380 290 372 340 376 376 H0 Z" fill="var(--magenta)"/>
  <path class="band-black" d="M0 0 H346 C390 40 400 130 385 210 C375 280 362 340 368 376 H0 Z" fill="var(--band-black)"/>
  <path class="card-face" d="M0 0 H311 C370 30 392 130 378 210 C368 280 356 340 362 376 H0 Z" fill="url(#fine-stripes)"/>

  <circle class="brand-circle" cx="178" cy="139" r="110" fill="var(--blush)" opacity="0.7"/>

  <text class="name" x="25" y="140" font-size="42" textLength="308" lengthAdjust="spacingAndGlyphs">Lucinda Parvell</text>
  <circle class="accent" cx="63" cy="160" r="1.8"/>
  <text class="tagline" x="72" y="164" font-size="12" textLength="124" lengthAdjust="spacingAndGlyphs">wellness wayfinder</text>
  <circle class="accent" cx="203" cy="160" r="1.8"/>
  <text class="credentials" x="242" y="181" font-size="12">CCH, CNP, MA</text>

  <rect class="social" x="34" y="270" width="17" height="17" rx="2" fill="var(--magenta)"/>
  <rect class="social" x="54" y="270" width="17" height="17" rx="2" fill="var(--magenta)"/>
  <rect class="social" x="74" y="270" width="17" height="17" rx="2" fill="var(--magenta)"/>

  <g class="icon-phone accent" transform="translate(34 299)">
    <path d="M1 3 C1 1 3 0 6 0 C9 0 11 1 11 3 L8.5 3.5 L8 2 H4 L3.5 3.5 Z"/>
    <rect x="2.5" y="4" width="7" height="4.5" rx="1"/>
  </g>
  <text class="contact" x="56" y="308" font-size="12">519-362-7015</text>

  <g class="icon-mail" transform="translate(34 323)">
    <rect width="12" height="8" rx="1" fill="var(--magenta)"/>
    <path d="M0.8 0.8 L6 4.8 L11.2 0.8" fill="none" stroke="var(--card-white)" stroke-width="1"/>
  </g>
  <text class="contact" x="56" y="331" font-size="12">lucinda@lucindaparvell.com</text>

  <text class="website" x="34" y="352" font-size="12.5">www.lucindaparvell.com</text>
</svg>
</body>
</html>
```